Vela Stewardship Business Card design

We need a creative business card design for our hospitality management company
We need the following information:
Our business Logo: Vela Stewardship
Name: Mara Dobrinsky
Phone number: 0458 317 642
Email: mara@velastewardship.com.au
Address: 214/53 Penrose Street, Harrow Bay 3261
Web: www.velastewardship.com.au
I need the design to be a working file so that I can insert the names and numbers of the other staff members of our business.
The cards need to be 90 x 40mm
Thanks
Industry/Entity Type
Hospitality
Look and feel

```html
<!DOCTYPE html>
<html lang="en">
<head>
<meta charset="utf-8">
<title>Vela Stewardship – Business Card</title>
<link rel="stylesheet" href="https://fonts.googleapis.com/css2?family=PT+Sans:wght@400&family=PT+Sans+Narrow:wght@400;700&display=swap">
<style>
  :root {
    --page: #ffffff;
    --navy: #072840;
    --white: #ffffff;
    --silver: #e4e7ea;
    --sky: #1ca8e3;
    --lime: #c5d500;
    --dash: #cfd6dc;
  }
  * { margin: 0; padding: 0; box-sizing: border-box; }
  html, body {
    width: 1200px; height: 897px; overflow: hidden;
    background: var(--page);
  }
  .canvas { position: relative; width: 1200px; height: 897px; }
  .card {
    position: absolute; left: 128px; top: 238px;
    width: 920px; height: 408px;
    background: var(--navy);
    color: var(--white);
  }
  .brand {
    position: absolute; left: 0; top: 0; width: 390px; height: 408px;
    text-align: center;
  }
  .brand-mark {
    position: absolute; left: 150px; top: 122px;
    width: 90px; height: 88px;
  }
  .brand-name {
    position: absolute; left: 0; right: 0; top: 221px;
    font: 700 37px/1 "PT Sans Narrow", sans-serif;
    letter-spacing: 0.5px;
    color: var(--silver);
  }
  .brand-web {
    position: absolute; left: 0; right: 0; top: 271px;
    font: 400 21px/1 "PT Sans", sans-serif;
    color: var(--lime);
  }
  .divider {
    position: absolute; left: 390px; top: 24px; height: 362px;
    border-left: 2px dashed var(--dash);
  }
  .person {
    position: absolute; left: 410px; width: 490px; top: 108px;
    text-align: center;
  }
  .person-name {
    font: 700 58px/1 "PT Sans Narrow", sans-serif;
    color: var(--white);
  }
  .person-email {
    margin-top: 6px;
    font: 400 23px/1 "PT Sans", sans-serif;
    color: var(--sky);
  }
  .contact {
    position: absolute; top: 320px;
    display: flex; align-items: flex-start; gap: 14px;
    font: 400 25px/34px "PT Sans Narrow", sans-serif;
    color: var(--white);
  }
  .contact-phone { left: 413px; }
  .contact-address { left: 623px; }
  .contact svg { flex: none; margin-top: 3px; }
</style>
</head>
<body>
<div class="canvas">
  <section class="card">
    <div class="brand">
      <svg class="brand-mark" viewBox="0 0 90 88" aria-hidden="true">
        <rect x="3" y="3" width="84" height="82" fill="none" stroke="var(--silver)" stroke-width="6"/>
      </svg>
      <div class="brand-name">VELA STEWARDSHIP</div>
      <div class="brand-web">www.velastewardship.com.au</div>
    </div>

    <div class="divider"></div>

    <div class="person">
      <div class="person-name">Mara Dobrinsky</div>
      <div class="person-email">mara@velastewardship.com.au</div>
    </div>

    <div class="contact contact-phone">
      <svg width="29" height="28" viewBox="0 0 29 28" aria-label="Phone">
        <rect x="0" y="0" width="29" height="28" rx="5" fill="var(--white)"/>
        <path d="M10 6c-2 1-3 3-2 6 1 4 4 8 8 10 2 1 4 0 5-1l-3-4-2 1c-2-1-3-3-4-5l2-1-2-5z" fill="var(--navy)"/>
      </svg>
      <span>0458 317 642</span>
    </div>

    <div class="contact contact-address">
      <svg width="33" height="31" viewBox="0 0 33 31" aria-label="Address">
        <path d="M16.5 2 1 16l2 2 13.5-12L30 18l2-2z" fill="var(--white)"/>
        <path d="M6 17 16.5 8 27 17v13h-7v-8h-7v8H6z" fill="var(--white)"/>
      </svg>
      <span>214/53 Penrose Street<br>Harrow Bay 3261</span>
    </div>
  </section>
</div>
</body>
</html>
```